Re-Brand of TindelMox along with a new website design

TindelMox Ltd are a software & database development company using technologies such as PHP, C#, HTML, JQuery, Flex, AS3, MySQL, Oracle, MSSQL. We like to target all types of business from small to large.

We are great at coding but rubbish at design so thats where we need your help!

We want a complete re-brand of TindelMox including logo, website design, and business cards.

We would like a design that is clean but other than that, please feel free to be creative.

****Logo****
We are looking for a logo that appears professional but with a splash of colour that indicates a creative side. Please see below some logos that we like the look of:

We like this one because it has a nice simple and clear font for the name of the company but also an icon which is colourful and stands out. http://markvault.example/2013/03/brivelo/

We like this one because it is very clean, simple and again very clear. http://markvault.example/2013/03/quantorels/

http://markvault.example/2013/03/tide-lamp/
http://markvault.example/2013/02/velmorin/
http://markvault.example/2013/01/art-gallery-tarnwick/

As you will see from all of these examples, the font is very clear but there is always a graphic representing the company too. This is what we like.

****Website****
These are some of the examples of websites we like:
https://www.zestrune.example/
https://www.chatterlane.example/home
http://www.haldenimagery.example/
http://www.vistor.example/
http://quillbay.example/
https://www.usebriefnest.example/personal-intros
http://www.marmotpanel.example/

The current site can be found at tindelmox.example.uk

Reason: We have extended the deadline of the project by 5 days as I realise the original deadline was very tight.

Software

Requirements
Must have
• Website must have the following pages
Home
Services
Projects
About Us
Contact Us

```html
<!DOCTYPE html>
<html lang="en">
<head>
<meta charset="utf-8">
<title>TindelMox — Software &amp; Database Development</title>
<link rel="stylesheet" href="https://fonts.googleapis.com/css2?family=PT+Sans:wght@400;700&family=PT+Sans+Narrow:wght@400;700&display=swap">
<style>
:root{
  --green-deep:#0e2b10;
  --green-dark:#153f18;
  --green-mid:#1f5a1e;
  --green-head:#2b5714;
  --green-btn:#1d4f12;
  --white:#ffffff;
  --text:#222222;
  --panel:#f4f4f4;
  --footer:#2e2e2e;
  --footer-text:#d8d8d8;
  --circle-edge:#e2e2e2;
  --label:#333333;
}
*{margin:0;padding:0;box-sizing:border-box}
html,body{width:1000px;height:1200px;overflow:hidden;background:var(--white)}
body{position:relative;font-family:"PT Sans",sans-serif;color:var(--text)}
.canvas{position:relative;width:1000px;height:1200px;overflow:hidden;
  background:linear-gradient(#eeeeee 413px,#ffffff 560px,#ffffff 980px,#eeeeee 1045px)}
.abs{position:absolute}

/* header */
.site-header{left:0;top:0;width:1000px;height:94px;
  background:linear-gradient(#184419,#123514);border-bottom:1px solid #2f6a2a}
.brand-dot{left:122px;top:12px;width:66px;height:66px;border-radius:50%;background:var(--white)}
.brand-name{left:196px;top:26px;font-family:"PT Sans Narrow",sans-serif;font-weight:700;
  font-size:35px;color:var(--white);letter-spacing:.5px;line-height:40px}
.search{left:654px;top:11px;display:flex}
.search-input{width:173px;height:19px;background:var(--white);border:1px solid #b9b9b9;
  font-size:10px;color:#999;padding:3px 0 0 16px}
.search-btn{width:53px;height:19px;background:var(--green-btn);color:#e8e8e8;font-size:10px;
  text-align:center;line-height:19px;letter-spacing:.3px}
.main-nav{left:488px;top:42px;display:flex;gap:6px}
.main-nav a{display:block;height:30px;border-radius:7px;border:2px solid #3e8a34;
  background:linear-gradient(#2d6420,#173f10);color:var(--white);text-decoration:none;
  font-family:"PT Sans Narrow",sans-serif;font-size:15px;line-height:26px;text-align:center}

/* hero */
.hero{left:0;top:94px;width:1000px;height:319px;
  background:radial-gradient(ellipse at 75% 30%,#2a5a22 0%,#173a16 40%,#07150a 75%,#050d06 100%)}
.hero-arrow{top:102px}
.hero-title{left:151px;top:174px;font-family:"PT Sans Narrow",sans-serif;font-weight:400;font-size:30px;color:var(--white);line-height:38px;white-space:nowrap}
.hero-copy{left:151px;top:221px;width:306px;font-size:11.5px;line-height:20px;color:#e9e9e9;text-align:justify}
.hero-visual{left:480px;top:137px;width:358px;height:200px;border-radius:6px;
  background:linear-gradient(135deg,#7a2525 0%,#4a7fbf 45%,#d8dde3 75%,#2a2f36 100%);opacity:.85}

/* content */
.panel{left:109px;top:392px;width:766px;height:160px;background:linear-gradient(#f4f4f4,#fbfbfb);border-top:1px solid #ddd}
.section-title{font-family:"PT Sans Narrow",sans-serif;font-weight:700;font-size:21px;color:var(--green-head);line-height:24px}
.welcome-title{left:127px;top:408px}
.welcome-visual{left:130px;top:447px;width:240px;height:118px;
  background:linear-gradient(90deg,#7b5a22 0%,#6a8fae 45%,#a02a2a 65%,#c8d4e2 100%);border-radius:3px}
.welcome-copy{left:388px;top:439px;width:480px;font-size:10.4px;line-height:13.5px;color:var(--text)}
.welcome-copy p{margin-bottom:13px}
.learn-more{left:793px;top:595px;width:68px;height:27px;background:var(--green-btn);border:1px solid #0d2c08;
  color:var(--white);font-family:"PT Sans Narrow",sans-serif;font-size:13px;text-align:center;line-height:25px}
.services-title{left:127px;top:617px}

.service{width:171px;height:171px;border-radius:50%;
  background:radial-gradient(circle at 50% 40%,#ffffff 55%,#f1f1f1 80%,#e4e4e4 100%);
  box-shadow:0 1px 3px rgba(0,0,0,.12),inset 0 0 0 1px var(--circle-edge);
  text-align:center}
.service-icon{position:absolute;left:50%;top:24px;width:78px;height:58px;margin-left:-39px;border-radius:8px}
.service-label{position:absolute;left:0;width:171px;font-family:"PT Sans Narrow",sans-serif;
  font-size:17px;line-height:25px;color:var(--label);text-transform:uppercase}

/* footer */
.site-footer{left:0;top:1045px;width:1000px;height:155px;background:var(--footer);color:var(--footer-text)}
.footer-title{font-family:"PT Sans Narrow",sans-serif;font-weight:400;font-size:18px;color:#f0f0f0}
.sitemap{left:140px;top:1090px;list-style:none;font-size:9.5px;line-height:20px;color:var(--footer-text)}
.sitemap li{position:relative}
.sitemap li::before{content:"›";position:absolute;left:-12px;top:-1px;font-size:12px;color:var(--footer-text)}
.footer-lines{font-size:9.5px;line-height:17.5px}
.social{left:769px;top:1073px;display:flex;gap:5px}
.social span{width:20px;height:20px;border-radius:50%;border:1px solid #bbb}
.copyright{left:700px;top:1106px;width:187px;text-align:right;font-size:9.5px}
</style>
</head>
<body>
<div class="canvas">

  <header class="site-header abs">
    <span class="brand-dot abs"></span>
    <div class="brand-name abs">TINDELMOX</div>
    <div class="search abs">
      <div class="search-input">type your word here</div>
      <div class="search-btn">SEARCH</div>
    </div>
    <nav class="main-nav abs">
      <a href="#" style="width:75px">Home</a>
      <a href="#" style="width:74px">About Us</a>
      <a href="#" style="width:85px">What We Do</a>
      <a href="#" style="width:74px">Projects</a>
      <a href="#" style="width:74px">Contact</a>
    </nav>
  </header>

  <section class="hero abs">
    <svg class="hero-arrow abs" style="left:80px" width="16" height="52" viewBox="0 0 16 52"><path d="M13 2 L3 26 L13 50" fill="none" stroke="#fff" stroke-width="3"/></svg>
    <svg class="hero-arrow abs" style="left:898px" width="16" height="52" viewBox="0 0 16 52"><path d="M3 2 L13 26 L3 50" fill="none" stroke="#fff" stroke-width="3"/></svg>
  </section>
  <h1 class="hero-title abs">Website Design &amp; Development</h1>
  <p class="hero-copy abs">Sed ut perspiciatis unde omnis iste natus error sit voluptatem accusantium doloremque laudantium, totam rem aperiam, eaque ipsa quae ab illo inven tore veritatis et quasi</p>
  <div class="hero-visual abs" role="img" aria-label="Fanned website screenshots beside a desktop monitor"></div>

  <div class="panel abs"></div>
  <h2 class="section-title welcome-title abs">WELCOME TO TINDELMOX</h2>
  <div class="welcome-visual abs" role="img" aria-label="Row of website page screenshots in perspective"></div>
  <div class="welcome-copy abs">
    <p>if you are looking for web, software, or IT services that really deliver but you don't want to pay over the odds then TindelMox is the right team for you.</p>
    <p>Based in Harlowmere our clients are both local, national, both large and small. You may be a start-up business in need of a 'get me up and running quickly' website, or a multi-million pound brand looking for an all singing, all dancing bespoke app.</p>
    <p>Maybe you are experiencing the pains and pleasures of growing your business and its time to improve your branding and to trade in your current home spun website for something more professional.</p>
    <p>Let's chat today about where we can take your business.</p>
  </div>
  <div class="learn-more abs">learn more</div>

  <h2 class="section-title services-title abs">WHAT WE DO</h2>

  <div class="service abs" style="left:144px;top:665px">
    <div class="service-icon" role="img" aria-label="Laptop with colourful puzzle pieces" style="background:linear-gradient(135deg,#3a8fd6,#e0c030,#7a7f88)"></div>
    <div class="service-label" style="top:95px">Website Design &amp;<br>Development</div>
  </div>
  <div class="service abs" style="left:337px;top:665px">
    <div class="service-icon" role="img" aria-label="Monitor and box of application icons" style="background:linear-gradient(135deg,#9cc6e8,#e9e9e9,#d94040)"></div>
    <div class="service-label" style="top:95px">Rich Internet<br>Applications</div>
  </div>
  <div class="service abs" style="left:529px;top:665px">
    <div class="service-icon" role="img" aria-label="Mobile phone and box of application icons" style="background:linear-gradient(135deg,#222,#e9e9e9,#3aa04a)"></div>
    <div class="service-label" style="top:95px">Mobile &amp; Tablet<br>Applications</div>
  </div>
  <div class="service abs" style="left:713px;top:665px">
    <div class="service-icon" role="img" aria-label="Pair of grey gears" style="background:linear-gradient(135deg,#c5c9cc,#8c9296)"></div>
    <div class="service-label" style="top:95px">Enterprise<br>Development</div>
  </div>

  <div class="service abs" style="left:144px;top:849px">
    <div class="service-icon" role="img" aria-label="Globe with database cylinders" style="background:linear-gradient(135deg,#2f86cf,#a9adb2)"></div>
    <div class="service-label" style="top:95px">Database<br>Development</div>
  </div>
  <div class="service abs" style="left:337px;top:849px">
    <div class="service-icon" role="img" aria-label="Report pages with a pen" style="background:linear-gradient(135deg,#eef2f8,#9fb0c6)"></div>
    <div class="service-label" style="top:95px">Database<br>Reporting</div>
  </div>
  <div class="service abs" style="left:529px;top:849px">
    <div class="service-icon" role="img" aria-label="Game controller" style="background:linear-gradient(135deg,#555,#222)"></div>
    <div class="service-label" style="top:107px">Games</div>
  </div>
  <div class="service abs" style="left:713px;top:849px">
    <div class="service-icon" role="img" aria-label="Laptop with chain and padlock" style="background:linear-gradient(135deg,#1a1a1a,#b8a98a)"></div>
    <div class="service-label" style="top:107px">IT Security</div>
  </div>

  <footer class="site-footer abs"></footer>
  <h3 class="footer-title abs" style="left:130px;top:1060px">Sitemap</h3>
  <ul class="sitemap abs">
    <li>Home</li><li>What We Do</li><li>Projects</li><li>About Us</li><li>Contact Us</li>
  </ul>
  <h3 class="footer-title abs" style="left:297px;top:1060px">Contact Us</h3>
  <div class="footer-lines abs" style="left:303px;top:1094px;color:var(--footer-text)">
    Address<br>42 Fenwick Lane<br>Harlowmere<br>Wendshire<br>HW4 7QZ
  </div>
  <div class="footer-lines abs" style="left:437px;top:1094px;color:var(--footer-text)">
    Telephone&nbsp; : &nbsp;01632 960 418<br>Email&nbsp; : &nbsp;contact@tindelmox.example.uk
  </div>
  <div class="social abs" aria-label="Social links">
    <span style="background:#2d5fa8"></span><span style="background:#3b7fc0"></span><span style="background:#3fb0e6"></span><span style="background:#3a3a3a"></span><span style="background:#c0262d"></span>
  </div>
  <div class="copyright abs" style="color:var(--footer-text)">© 2013 TindelMox, All Rights Reserved</div>

</div>
</body>
</html>
```